IT company requires website redesign

I have an old boring website that I want to update - www.tvkb-example.net
I am a growing IT company beginning to look after more healthcare professionals such as medical and dental practices so a more professional look is required

Blue and orange are the company colours. See one of our local competitors for your reference and ideas - https://www.plinth-halvard.example.au

Target Market(s)

Medical, dental, professional, solicitors etc

Industry/Entity Type

It Support

Number of Pages Required

5+ page

Colors

Designer to choose colors to be used in the design.

Requirements
Must have
• Classy feel, simple with the 'less is more' approach
• On support page, links to support items, a couple more to come
• Reference to our technology partners
• Easy to read
Nice to have
• Company colours are blue with a little orange but I willing to consider new web colour schemes
• leave the rest to you

```html
<!DOCTYPE html>
<html lang="en">
<head>
<meta charset="utf-8">
<title>Corvane Integrated – IT Support</title>
<link href="https://fonts.googleapis.com/css2?family=Lato:wght@300;400;700;900&family=Roboto+Condensed:wght@400;700&display=swap" rel="stylesheet">
<style>
:root{
  --navy:#1d3a7a;
  --blue:#2b4a96;
  --orange:#e0672a;
  --orange-dark:#c9541c;
  --ink:#333a44;
  --muted:#6b7079;
  --line:#e2e4e8;
  --light:#f4f5f7;
  --dark:#2f3033;
  --darker:#262729;
  --white:#ffffff;
}
*{box-sizing:border-box;margin:0;padding:0}
html,body{width:1200px;height:4839px;overflow:hidden}
body{font-family:"Lato",Arial,sans-serif;color:var(--ink);background:var(--white);font-size:15px;line-height:1.5}
.wrap{width:970px;margin:0 auto;position:relative}
.section-title{font-weight:700;color:var(--navy);font-size:30px;text-align:center;letter-spacing:.2px}
.btn-outline{display:inline-block;border:2px solid var(--orange);color:var(--orange);border-radius:20px;padding:6px 26px;font-size:14px}
.btn{display:inline-block;background:var(--orange);color:var(--white);border-radius:20px;padding:8px 30px;font-weight:700;font-size:15px}

/* header */
.topbar{height:34px;border-bottom:1px solid var(--line)}
.topbar .wrap{display:flex;align-items:center;height:34px;justify-content:space-between;font-size:12px;color:var(--muted)}
.topbar .contact{display:flex;gap:26px;align-items:center}
.topbar .contact span{display:flex;align-items:center;gap:7px}
.topbar .social{display:flex;gap:8px}
.dot{width:18px;height:18px;border:1px solid #c5c8ce;border-radius:50%}
.nav{height:96px}
.nav .wrap{display:flex;align-items:center;height:96px;justify-content:space-between}
.brand{display:flex;align-items:center;gap:10px;font-weight:900;color:var(--navy);font-size:24px;line-height:1}
.brand i{width:16px;height:16px;border-radius:50%;background:var(--orange)}
.menu{display:flex;gap:52px;font-size:15px;font-weight:700;color:var(--navy)}
.menu .active{color:var(--orange)}

/* hero */
.hero{height:547px;position:relative;overflow:hidden}
.hero-photo{position:absolute;inset:0;background:linear-gradient(100deg,#ddd5cc 0%,#efeae4 35%,#e2ddd6 60%,#cdc8c2 100%)}
.hero-circle{position:absolute;left:630px;top:45px;width:455px;height:455px;border-radius:50%;background:rgba(96,96,100,.88);display:flex;align-items:center;justify-content:center;text-align:center;padding:50px 55px}
.hero-circle h1{font-family:"Roboto Condensed",Arial,sans-serif;font-weight:400;color:var(--white);font-size:34px;line-height:1.22}
.hero-arrow{position:absolute;top:258px;right:12px}

/* help band */
.help{height:194px;background:var(--light)}
.help .wrap{display:flex;align-items:center;justify-content:space-between;height:194px;padding:0 50px}
.help h2{font-size:36px;font-weight:900;color:var(--navy);line-height:1.1}
.help p{font-size:16px;font-weight:700;color:var(--ink);margin-top:4px}
.call{display:flex;align-items:center;gap:12px;background:var(--orange);border-radius:8px;padding:12px 20px;color:var(--white)}
.call small{display:block;font-size:14px;font-weight:700;letter-spacing:.5px}
.call strong{display:block;font-size:30px;font-weight:900;line-height:1}

/* services */
.services{height:758px;padding-top:85px}
.cards{display:grid;grid-template-columns:repeat(4,226px);gap:22px 22px;margin-top:68px}
.card{height:226px;border:1px solid var(--line);text-align:center;padding:22px 18px}
.card.is-active{border-color:var(--orange)}
.card .ico{width:64px;height:64px;margin:0 auto 10px;border-radius:50%;border:1px solid var(--line);display:flex;align-items:center;justify-content:center}
.card.is-active .ico{background:var(--orange);border-color:var(--orange)}
.card h3{font-size:16px;font-weight:700;color:var(--navy);margin-bottom:6px}
.card.is-active h3{color:var(--orange)}
.card p{font-size:12px;color:var(--muted);line-height:1.45}

/* about */
.about{height:445px;background:var(--dark);color:var(--white);text-align:center;padding-top:85px}
.about h2{font-size:30px;font-weight:700}
.about .lead{font-weight:700;font-size:15px;margin-top:34px}
.about p{font-size:15px;color:#dcdcdc;max-width:880px;margin:14px auto 0}
.about .btn-outline{margin-top:26px}

/* savings */
.save{height:629px}
.save .wrap{display:flex;justify-content:space-between;padding-top:90px}
.save-text{width:570px}
.save h2{font-size:36px;font-weight:900;color:var(--navy)}
.save .intro{margin-top:22px;font-size:15px}
.save ul{margin:10px 0 0 18px;font-size:15px;line-height:1.75}
.save .btn-outline{margin-top:16px}
.save-photo{width:403px;height:430px;margin-top:12px;background:linear-gradient(150deg,#22324d,#4b6d9a 50%,#1a2840)}

/* cta */
.cta{height:297px;background:linear-gradient(90deg,#1f3672,#3a5aa8);color:var(--white);text-align:center;padding-top:88px}
.cta h2{font-size:32px;font-weight:900}
.cta p{font-size:28px;font-weight:300;margin-top:2px}
.cta .btn{margin-top:18px}

/* testimonials */
.testimonials{height:539px;padding-top:95px;text-align:center}
.avatar{width:130px;height:130px;border-radius:50%;margin:58px auto 0;background:radial-gradient(circle at 50% 40%,#d6d1cb,#9ea3aa)}
.testimonials blockquote{font-size:13px;color:var(--muted);width:920px;margin:36px auto 0;line-height:1.6}
.testimonials .name{font-weight:700;color:var(--navy);font-size:16px;margin-top:18px}
.testimonials .role{font-size:13px}

/* partners */
.partners{height:342px;background:var(--light);padding-top:90px}
.logos{display:flex;align-items:center;gap:18px;justify-content:center;margin-top:50px}
.logo-badge{width:140px;height:80px;background:var(--white);display:flex;align-items:center;justify-content:center}
.logo-badge span{width:70px;height:34px;border-radius:4px;background:#c7cbd2}

/* contact */
.contact-us{height:813px;background:var(--darker);color:var(--white);text-align:center;padding-top:78px}
.contact-us .kicker{color:var(--orange);font-size:13px;letter-spacing:2px}
.contact-us h2{font-size:32px;font-weight:900}
.contact-us .blurb{font-size:13px;color:#c9c9c9;width:620px;margin:8px auto 0}
.info{display:flex;justify-content:center;gap:60px;margin-top:50px}
.info-box{width:260px;height:152px;background:rgba(255,255,255,.06);padding-top:28px}
.info-box h4{font-size:16px;margin-top:10px}
.info-box p{font-size:15px;color:#e5e5e5}
.form{width:885px;margin:28px auto 0;background:rgba(255,255,255,.05);padding:44px 30px 0;height:310px}
.row{display:flex;gap:30px;margin-bottom:18px}
.field{flex:1;height:36px;border:1px solid #5b5c60;border-radius:3px;text-align:left;padding:8px 12px;font-size:13px;color:#a8a8a8}
.field.tall{height:78px}
.form .btn{margin-top:4px}

/* footer */
.footer{height:145px;background:var(--orange);text-align:center;color:var(--white);padding-top:42px}
.footer .social{display:flex;gap:12px;justify-content:center}
.footer .dot{width:30px;height:30px;border-color:rgba(255,255,255,.8)}
.footer p{font-size:12px;margin-top:12px}
</style>
</head>
<body>

<header>
  <div class="topbar"><div class="wrap">
    <div class="contact">
      <span><svg width="12" height="12" viewBox="0 0 24 24"><path fill="#e0672a" d="M6.6 10.8a15 15 0 0 0 6.6 6.6l2.2-2.2a1 1 0 0 1 1-.25 11.4 11.4 0 0 0 3.6.6 1 1 0 0 1 1 1V20a1 1 0 0 1-1 1A17 17 0 0 1 3 4a1 1 0 0 1 1-1h3.5a1 1 0 0 1 1 1c0 1.25.2 2.45.6 3.6a1 1 0 0 1-.25 1z"/></svg>1300 482 617</span>
      <span><svg width="13" height="10" viewBox="0 0 26 20"><rect x="1" y="1" width="24" height="18" fill="#e0672a"/><path d="M1 1l12 10L25 1" stroke="#fff" stroke-width="2" fill="none"/></svg>info@tvkb-example.net</span>
    </div>
    <div class="social"><i class="dot"></i><i class="dot"></i><i class="dot"></i><i class="dot"></i></div>
  </div></div>
  <nav class="nav"><div class="wrap">
    <div class="brand"><i></i>Corvane Integrated</div>
    <div class="menu"><span class="active">Home</span><span>Our Services</span><span>About Us</span><span>Our Team</span><span>Contact Us</span><span>Support</span></div>
  </div></nav>
</header>

<section class="hero">
  <div class="hero-photo" role="img" aria-label="Photo of a smiling professional woman working on a laptop in a bright office"></div>
  <div class="hero-circle"><h1>Corvane Integrated where we believe that a better tomorrow, starts through intelligent use of technology today!</h1></div>
  <svg class="hero-arrow" width="14" height="26" viewBox="0 0 14 26"><path d="M2 2l10 11L2 24" stroke="#fff" stroke-width="2" fill="none"/></svg>
</section>

<section class="help"><div class="wrap">
  <div><h2>We Are Here To Help You!</h2><p>A Better Tomorrow, Through Intelligent use of Technology Today!</p></div>
  <div class="call">
    <svg width="40" height="40" viewBox="0 0 40 40"><circle cx="20" cy="20" r="18" fill="none" stroke="#fff" stroke-width="2"/><text x="20" y="25" text-anchor="middle" font-size="12" font-weight="700" fill="#fff" font-family="Lato,sans-serif">24/7</text></svg>
    <div><small>CALL US TODAY!</small><strong>1300 482 617</strong></div>
  </div>
</div></section>

<section class="services"><div class="wrap">
  <h2 class="section-title">Our Services</h2>
  <div class="cards">
    <div class="card"><div class="ico"><svg width="30" height="30" viewBox="0 0 30 30"><rect x="3" y="5" width="24" height="16" fill="none" stroke="#2b4a96" stroke-width="2"/><path d="M10 26h10M15 21v5" stroke="#2b4a96" stroke-width="2"/></svg></div><h3>Software</h3><p>Integrated software with the tools, capabilities and expertise to guide any organisation with their software requirements.</p></div>
    <div class="card is-active"><div class="ico"><svg width="30" height="30" viewBox="0 0 30 30"><rect x="4" y="5" width="22" height="16" fill="none" stroke="#fff" stroke-width="2"/><path d="M9 26h12" stroke="#fff" stroke-width="2"/></svg></div><h3>Products</h3><p>We will determine and provide appropriate products and services to address your technology requirements.</p></div>
    <div class="card"><div class="ico"><svg width="30" height="30" viewBox="0 0 30 30"><rect x="5" y="6" width="20" height="14" fill="none" stroke="#2b4a96" stroke-width="2"/><path d="M8 24h14" stroke="#e0672a" stroke-width="2"/></svg></div><h3>Solutions</h3><p>A full range of IT solutions, including carefully selected IT service partners to minimise risk and improve continuity.</p></div>
    <div class="card"><div class="ico"><svg width="30" height="30" viewBox="0 0 30 30"><rect x="3" y="8" width="24" height="14" fill="none" stroke="#2b4a96" stroke-width="2"/><circle cx="15" cy="15" r="3" fill="#e0672a"/></svg></div><h3>Finance – Easy Lease</h3><p>Concerned about your budget? We can help you with flexible payment plan options.</p></div>
    <div class="card"><div class="ico"><svg width="30" height="30" viewBox="0 0 30 30"><rect x="3" y="5" width="24" height="16" fill="none" stroke="#2b4a96" stroke-width="2"/><path d="M12 10l-3 3 3 3M18 10l3 3-3 3" stroke="#e0672a" stroke-width="2" fill="none"/></svg></div><h3>Programming</h3><p>Electronic design manufacturing and microprocessor programming.</p></div>
    <div class="card"><div class="ico"><svg width="30" height="30" viewBox="0 0 30 30"><rect x="5" y="10" width="20" height="12" fill="none" stroke="#2b4a96" stroke-width="2"/><path d="M9 10V5h12v5M9 22v3h12v-3" stroke="#e0672a" stroke-width="2" fill="none"/></svg></div><h3>Copiers</h3><p>B&amp;W Photocopiers &amp; MFP with full integration into networks for printing and scanning.</p></div>
    <div class="card"><div class="ico"><svg width="30" height="30" viewBox="0 0 30 30"><rect x="4" y="11" width="22" height="10" fill="none" stroke="#2b4a96" stroke-width="2"/><path d="M9 11V5h12v6M9 21v4h12v-4" stroke="#2b4a96" stroke-width="2" fill="none"/></svg></div><h3>Printers &amp; Scanners</h3><p>Colour copiers, inkjet printers &amp; integration into networks for printing and scanning.</p></div>
    <div class="card"><div class="ico"><svg width="30" height="30" viewBox="0 0 30 30"><circle cx="15" cy="15" r="10" fill="none" stroke="#2b4a96" stroke-width="2"/><path d="M5 15h20M15 5c-4 5-4 15 0 20M15 5c4 5 4 15 0 20" stroke="#e0672a" stroke-width="1.5" fill="none"/></svg></div><h3>Web Hosting &amp; Design</h3><p>Our team of specialised staff are ready and waiting to assist you with all your website design and hosting needs.</p></div>
  </div>
</div></section>

<section class="about"><div class="wrap">
  <h2>About Corvane Integrated</h2>
  <p class="lead">Welcome to Corvane Integrated where we believe that a better tomorrow, starts through intelligent use of technology today!</p>
  <p>Corvane Integrated is a value added Information technology company supplying and implementing hardware and software that are complemented by the provision of associated support services and solutions.</p>
  <p>We ensure that the risks associated with the deployment of new technologies are reduced, while providing a competitive total cost of IT ownership that yields a compelling return on investment.</p>
  <span class="btn-outline">Read More »</span>
</div></section>

<section class="save"><div class="wrap">
  <div class="save-text">
    <h2>How we can save you $$$</h2>
    <p class="intro">We pride ourselves in offering only the best solutions, with our diverse skill set in areas including:</p>
    <ul>
      <li>Medical Software including ClinicDesk, PracticeLedger and CarePoint. We can also assist with eCPS compliance.</li>
      <li>Legal packages including CaseVault</li>
      <li>Terminal Services RDP connections</li>
      <li>Hosted mail server</li>
      <li>NAS installations</li>
      <li>Cloud based solutions</li>
      <li>Virtualisation</li>
      <li>Data recovery</li>
      <li>Virus prevention and removal</li>
    </ul>
    <span class="btn-outline">Read More »</span>
  </div>
  <div class="save-photo" role="img" aria-label="Photo of two IT technicians with a laptop in a server room"></div>
</div></section>

<section class="cta">
  <h2>A Better Tomorrow, Through Intelligent use of Technology Today</h2>
  <p>Contact our Specialised Team Now!</p>
  <span class="btn">CALL US TODAY! »</span>
</section>

<section class="testimonials"><div class="wrap">
  <h2 class="section-title">Client Testimonials</h2>
  <div class="avatar" role="img" aria-label="Portrait photo of the client"></div>
  <blockquote>Corvane Integrated have been our IT support company for over 10 years. So why do we stick with them? Because they are awesome! The team is consistently able to solve our many and varied problems. Whether we phone about server functionality, email capacity, software issues or IT security, the staff are always able to provide a quick and efficient response, leaving us to get on with our business.</blockquote>
  <p class="name">Mirela Oakes</p>
  <p class="role">Administration Manager</p>
</div></section>

<section class="partners"><div class="wrap">
  <h2 class="section-title">Our Partners</h2>
  <div class="logos">
    <svg width="14" height="24" viewBox="0 0 14 24"><path d="M12 2L2 12l10 10" stroke="#9aa0a8" stroke-width="2" fill="none"/></svg>
    <div class="logo-badge"><span></span></div>
    <div class="logo-badge"><span></span></div>
    <div class="logo-badge"><span></span></div>
    <div class="logo-badge"><span></span></div>
    <div class="logo-badge"><span></span></div>
    <div class="logo-badge"><span></span></div>
    <svg width="14" height="24" viewBox="0 0 14 24"><path d="M2 2l10 10L2 22" stroke="#9aa0a8" stroke-width="2" fill="none"/></svg>
  </div>
</div></section>

<section class="contact-us"><div class="wrap">
  <p class="kicker">GET IN TOUCH</p>
  <h2>CONTACT US</h2>
  <p class="blurb">Send us a note and our friendly support team will reply within one business day to help you plan your next step.</p>
  <div class="info">
    <div class="info-box"><svg width="34" height="34" viewBox="0 0 24 24"><path fill="#e0672a" d="M6.6 10.8a15 15 0 0 0 6.6 6.6l2.2-2.2a1 1 0 0 1 1-.25 11.4 11.4 0 0 0 3.6.6 1 1 0 0 1 1 1V20a1 1 0 0 1-1 1A17 17 0 0 1 3 4a1 1 0 0 1 1-1h3.5a1 1 0 0 1 1 1c0 1.250.2 2.45.6 3.6a1 1 0 0 1-.25 1z"/></svg><h4>Phone</h4><p>1300 482 617</p></div>
    <div class="info-box"><svg width="34" height="34" viewBox="0 0 24 24"><path fill="#e0672a" d="M12 2a7 7 0 0 0-7 7c0 5 7 13 7 13s7-8 7-13a7 7 0 0 0-7-7zm0 9.5A2.5 2.5 0 1 1 12 6.5a2.5 2.5 0 0 1 0 5z"/></svg><h4>Address</h4><p>12 Belford Lane, Tarrow QLD 4390</p></div>
    <div class="info-box"><svg width="34" height="34" viewBox="0 0 26 22"><rect x="1" y="3" width="24" height="18" fill="#e0672a"/><path d="M1 3l12 10L25 3" stroke="#262729" stroke-width="2" fill="none"/></svg><h4>Email</h4><p>info@tvkb-example.net</p></div>
  </div>
  <div class="form">
    <div class="row"><div class="field">Your Name</div><div class="field">Phone</div></div>
    <div class="row"><div class="field">Email</div></div>
    <div class="row"><div class="field tall">Your Message</div></div>
    <span class="btn">SUBMIT »</span>
  </div>
</div></section>

<footer class="footer">
  <div class="social"><i class="dot"></i><i class="dot"></i><i class="dot"></i><i class="dot"></i></div>
  <p>Copyright © 2019 Corvane Integrated . All Rights Reserved.</p>
</footer>

</body>
</html>
```